Business website cyber security

Full redesign of our current business website, mockup and powerpoint presentation have been provided.
Some animated elements (example: SVG with CSS) are welcome.
A detailed requirement list can also be found in the attached powerpoint
Also uploaded is the current page as a nicepage & html export. All 11 sites shall be reworked. "Branches", "Download", "Contact" and "Legal Information" are not needed .

A good example of a competitor is https://www.fennotrix.de/ this. Not in terms of colors, but in regard to website structure, animated elements and overall look.

Target Market(s)

Cyber security for the B2B market

Industry/Entity Type

IT, IT Security, banking

Coding

Coded - Design and coding required

Number of Pages Required

5+ page

Other font styles liked:
• ReadexPro Regular, ReadexPro Light

Colors
0054AA
0677BA
7BADD7
CADEEF
E8F1F8

Requirements
Must have
• Modern and sleek design, corporate identity
Nice to have
• Animated elements (css svg)
Should not have
• too many colors (max 4), too fancy

```html
<!DOCTYPE html>
<html lang="en">
<head>
<meta charset="utf-8">
<title>Korvanta S.à r.l. – IT Security & Compliance</title>
<link href="https://fonts.googleapis.com/css2?family=Exo+2:wght@300;400;700;800&family=Readex+Pro:wght@300;400;500;600&display=swap" rel="stylesheet">
<style>
:root{
  --navy:#0b2f7c;
  --blue:#0054AA;
  --mid:#0677BA;
  --sky:#2e8fd6;
  --pale:#7BADD7;
  --mist:#CADEEF;
  --ice:#E8F1F8;
  --white:#ffffff;
  --ink:#1d2740;
  --footer:#1c4593;
}
*{box-sizing:border-box;margin:0;padding:0}
html,body{width:1200px;height:3271px;overflow:hidden}
body{position:relative;background:var(--white);font-family:"Readex Pro",sans-serif;color:var(--ink)}
.abs{position:absolute}
.heading{font-family:"Exo 2",sans-serif}

/* header */
.site-header{position:absolute;left:0;top:0;width:1200px;height:96px;background:var(--white);z-index:3}
.brand{position:absolute;left:122px;top:5px;width:130px;height:130px;border-radius:50%;background:var(--white);border:3px solid var(--navy);display:flex;align-items:center;justify-content:center;z-index:4}
.brand span{font-family:"Readex Pro",sans-serif;font-weight:600;font-size:20px;color:var(--blue)}
.main-nav{position:absolute;top:48px;left:0;width:1200px;font-size:12.5px;letter-spacing:.3px;color:var(--ink)}
.main-nav a{position:absolute;color:inherit;text-decoration:none}
.lang{position:absolute;left:1038px;top:46px}

/* hero */
.hero{position:absolute;left:0;top:96px;width:1200px;height:544px;background:linear-gradient(100deg,#0a2d70 0%,#0c3a86 40%,#0a4f9a 70%,#0b6bb8 100%);overflow:hidden}
.hero-visual{position:absolute;left:520px;top:0;width:680px;height:544px;background:radial-gradient(circle at 45% 50%,rgba(90,220,255,.55) 0%,rgba(20,120,200,.35) 30%,rgba(10,50,120,0) 70%)}
.hero-title{position:absolute;left:138px;top:134px;font-family:"Exo 2",sans-serif;font-weight:300;font-size:38px;color:var(--white);letter-spacing:1px}
.hero-sub{position:absolute;left:138px;top:184px;font-family:"Exo 2",sans-serif;font-weight:700;font-size:20px;color:var(--white)}
.hero-text{position:absolute;left:138px;top:216px;width:380px;font-size:13px;line-height:20px;color:var(--white)}

/* about */
.about{position:absolute;left:0;top:640px;width:1200px;height:674px;background:linear-gradient(180deg,#fafcfe,#ffffff)}
.eyebrow{position:absolute;left:0;width:1200px;text-align:center;font-family:"Exo 2",sans-serif;font-weight:300;font-size:19px;text-transform:uppercase}
.section-title{position:absolute;left:0;width:1200px;text-align:center;font-family:"Exo 2",sans-serif;font-weight:800;font-size:32px;letter-spacing:1px}
.about .eyebrow{top:62px;color:var(--blue)}
.about .section-title{top:88px;color:var(--navy)}
.about-frame{position:absolute;left:113px;top:169px;width:298px;height:248px;background:linear-gradient(90deg,var(--navy),var(--blue) 70%,var(--sky))}
.about-photo{position:absolute;left:128px;top:183px;width:442px;height:375px;background:linear-gradient(135deg,#1d4a8f,#4a7fb8 45%,#9ab8d8 75%,#2d5a9c)}
.dots{position:absolute}
.about-text{position:absolute;left:629px;top:180px;width:470px;font-size:14px;line-height:23px;color:var(--ink)}
.about-text p+p{margin-top:10px}

/* history */
.history{position:absolute;left:0;top:1314px;width:1200px;height:800px;background:linear-gradient(180deg,#0d3d8e 0%,#0c3f92 55%,#114aa0 62%,#0c3f92 75%,#0b3a8a 100%);overflow:hidden}
.history-glow{position:absolute;left:-100px;top:440px;width:1400px;height:180px;background:radial-gradient(ellipse at 50% 50%,rgba(120,200,255,.35),rgba(60,140,230,.12) 45%,rgba(0,0,0,0) 70%)}
.history .eyebrow{top:88px;color:var(--white);font-size:16px}
.history .section-title{top:108px;color:var(--white)}
.history-text{position:absolute;left:172px;top:164px;width:856px;text-align:center;font-size:14px;line-height:23px;color:var(--white)}
.history-text p+p{margin-top:11px}
.history-text p.spaced{margin-top:46px}

/* timeline */
.timeline{position:absolute;left:160px;top:1888px;width:911px;height:371px;background:var(--white);box-shadow:0 4px 14px rgba(10,40,100,.18)}
.track{position:absolute;top:179px;height:35px}
.track span{position:absolute;top:0;height:35px;width:140px;clip-path:polygon(0 0,88% 0,100% 50%,88% 100%,0 100%,7% 50%);color:var(--white);font-weight:600;font-size:16px;display:flex;align-items:center;justify-content:center;padding-right:10px}
.track span.dark{background:var(--navy)}
.track span.light{background:var(--sky)}
.track span.first{clip-path:polygon(0 0,88% 0,100% 50%,88% 100%,0 100%)}
.milestone{position:absolute;width:130px;margin-left:-65px;text-align:center;font-size:12.5px;line-height:18px;text-transform:uppercase}
.milestone.top{color:var(--sky)}
.milestone.bottom{color:var(--navy)}
.hex{position:absolute;width:76px;height:84px;margin-left:-38px}
.stem{position:absolute;width:0;border-left:1.5px dashed var(--pale)}

/* company section */
.company-title{position:absolute;left:152px;top:2368px;font-family:"Exo 2",sans-serif;font-weight:800;font-size:31px;color:var(--navy);letter-spacing:2px}
.company-text{position:absolute;left:152px;top:2438px;width:472px;font-size:14.5px;line-height:27px;color:var(--blue)}
.company-visual{position:absolute;left:650px;top:2314px;width:438px;height:484px}

/* footer */
.site-footer{position:absolute;left:0;top:2887px;width:1200px;height:384px;background:var(--footer);color:var(--white)}
.footer-brand{position:absolute;left:118px;top:56px;width:144px;height:144px;border-radius:50%;background:var(--white);border:3px solid var(--navy);display:flex;align-items:center;justify-content:center}
.footer-brand span{font-weight:600;font-size:22px;color:var(--blue)}
.col-rule{position:absolute;top:15px;width:1px;height:210px;background:rgba(255,255,255,.25)}
.col-rule::before{content:"";position:absolute;left:-1px;top:65px;width:3px;height:20px;background:var(--sky)}
.col-head{position:absolute;top:75px;font-weight:600;font-size:13.5px;letter-spacing:.3px}
.col-links{position:absolute;top:110px;list-style:none;font-size:11.5px;line-height:24.8px;color:var(--mist)}
.contact-item{position:absolute;display:flex;align-items:center;gap:12px}
.contact-item .ic{width:30px;height:30px;border-radius:50%;background:var(--white);display:flex;align-items:center;justify-content:center}
.contact-item small{display:block;font-size:11px;color:var(--mist)}
.contact-item b{display:block;font-weight:400;font-size:13.5px}
.socials{position:absolute;left:938px;top:108px;display:flex;gap:6px}
.socials i{display:block;width:28px;height:28px;border-radius:50%;border:2px solid var(--white)}
.footer-rule{position:absolute;left:0;top:294px;width:1200px;height:1px;background:rgba(255,255,255,.2)}
.copyright{position:absolute;left:132px;top:320px;font-size:11px;color:var(--mist)}
.legal-links{position:absolute;right:142px;top:318px;font-size:11px;color:var(--mist)}

@keyframes pulse{0%,100%{opacity:.6}50%{opacity:1}}
.hero-visual{animation:pulse 4s ease-in-out infinite}
</style>
</head>
<body>

<header class="site-header">
  <nav class="main-nav">
    <a style="left:311px">HOME</a>
    <a style="left:377px">CDAAS</a>
    <a style="left:450px">SECURITY SERVICES</a>
    <a style="left:613px">COMPLIANCE</a>
    <a style="left:733px">UNTEREHMEN</a>
    <a style="left:855px">KARRIERE</a>
    <a style="left:954px">KONTAKT</a>
  </nav>
  <svg class="lang" width="40" height="20" viewBox="0 0 40 20" aria-label="Language: English">
    <circle cx="10" cy="10" r="9" fill="#1f3a8a"/>
    <path d="M10 1v18M1 10h18" stroke="#fff" stroke-width="4"/>
    <path d="M10 1v18M1 10h18" stroke="#c8102e" stroke-width="2"/>
    <path d="M26 8l4 4 4-4z" fill="#7a8aa8"/>
  </svg>
  <svg class="abs" style="left:328px;top:24px" width="8" height="22" viewBox="0 0 8 22"><g fill="var(--sky)"><circle cx="4" cy="3" r="1.6"/><circle cx="2" cy="9" r="1.6"/><circle cx="6" cy="9" r="1.6"/><circle cx="4" cy="15" r="1.6"/></g></svg>
</header>
<div class="brand"><span>Korvanta</span></div>

<section class="hero">
  <div class="hero-visual" role="img" aria-label="Photo of a hand touching a glowing digital padlock shield interface"></div>
  <h1 class="hero-title">KORVANTA S.À R.L</h1>
  <h2 class="hero-sub">PHILOSOPHIE</h2>
  <p class="hero-text">We only accept orders from subject areas that we can safely cover professionally. Our consultants have well-founded specialist theoretical training and further education and have both feet on the ground in practice. We value clear communication and when looking for suitable and practical solutions, we sometimes think outside the box. If a task requires it, we also think outside the box, without wanting to bang our heads against the wall. We are only satisfied when our customers are satisfied. We keep what we promise.</p>
</section>

<section class="about">
  <p class="eyebrow">About us</p>
  <h2 class="section-title">WHO WE ARE</h2>
  <div class="about-frame"></div>
  <div class="about-photo" role="img" aria-label="Photo of a consultant working at a laptop with security padlock graphics overlaid"></div>
  <svg class="dots" style="left:436px;top:418px" width="170" height="170" viewBox="0 0 170 170" aria-hidden="true">
    <defs><pattern id="dotgrid" width="14" height="14" patternUnits="userSpaceOnUse"><circle cx="3" cy="3" r="1.8" fill="var(--pale)"/></pattern></defs>
    <rect x="138" y="0" width="30" height="170" fill="url(#dotgrid)"/>
    <rect x="0" y="140" width="170" height="30" fill="url(#dotgrid)"/>
  </svg>
  <div class="about-text">
    <p>We are a company specializing in IT security and compliance. Our employees are highly trained, are subject to permanent further training in order to always meet the highest requirements and are among the best in Europe. In addition to optimal accessibility, our established Security Operation Center (SOC) in Luxembourg also offers support for security monitoring services for IT infrastructures with various technologies (Logvera, QSentry, Watchtide, Datafold, Scanrift, Shieldmark, Tracewire, Vulnly).</p>
    <p>We serve services from a complex SIEM infrastructure to vulnerability management. We also use security-related information to create use cases and technical monitoring reports. This enables the integration of automatisms that are based on existing infrastructure components, such as e.g. B. Docspace, map a cost-effective eGRC. However, our field of activity also includes tender preparation, support and implementation of projects for security services, implementation and run of e.g. SOC, IAM or PUM services.</p>
  </div>
</section>

<section class="history">
  <div class="history-glow" role="img" aria-label="Glowing digital particle wave"></div>
  <p class="eyebrow">Our history</p>
  <h2 class="section-title">HISTORY</h2>
  <div class="history-text">
    <p>The Korvanta S.à r.l. is from the Korvanta GmbH emerged, which was initially founded in 2000 in Frankfurt am Main as a platform for project-related collaboration by freelancers. In the founding years, the aim was to create a structure that would network the partners with each other and thus offer customers a wide-ranging portfolio of different services. The successful development led to the initially rather loose organization becoming more and more solidified, structured and focused. In the last 12 years, the issues of security and compliance for the financial industry have become the heart of society. This concentration of topics was ultimately the decisive factor in relocating the company headquarters to Luxembourg. The Luxembourg market offers numerous advantages for the financial industry, since many counterparts of the financial houses established in Germany also exist in Luxembourg, but the banking supervisory authority based there has strict regulatory requirements with regard to cross-border access to customer systems in Luxembourg.</p>
    <p>The experience gained on the Luxembourg and German financial markets has helped the Korvanta to become a preferred partner for security and compliance services for well-known financial customers and the established IT outsourcers in the DACH region.</p>
    <p class="spaced">The result of this development today is a focused service provider that is networked in the market and has established itself as a highly specialized and customer-oriented problem solver in the area of security and application services.</p>
  </div>
</section>

<div class="timeline">
  <svg width="0" height="0" style="position:absolute">
    <defs>
      <symbol id="hex-dark" viewBox="0 0 76 84"><polygon points="38,2 73,22 73,62 38,82 3,62 3,22" fill="none" stroke="var(--navy)" stroke-width="2"/><polygon points="38,9 67,26 67,58 38,75 9,58 9,26" fill="var(--navy)"/></symbol>
      <symbol id="hex-light" viewBox="0 0 76 84"><polygon points="38,2 73,22 73,62 38,82 3,62 3,22" fill="none" stroke="var(--sky)" stroke-width="2"/><polygon points="38,9 67,26 67,58 38,75 9,58 9,26" fill="var(--sky)"/></symbol>
    </defs>
  </svg>

  <div class="track" style="left:47px">
    <span class="dark first" style="left:0">2000</span>
    <span class="light" style="left:134px">2006</span>
    <span class="dark" style="left:268px">2010</span>
    <span class="light" style="left:402px">2013</span>
    <span class="dark" style="left:536px">2018</span>
    <span class="light" style="left:670px">2019</span>
  </div>

  <!-- top milestones -->
  <div class="stem" style="left:116px;top:130px;height:48px"></div>
  <svg class="hex" style="left:116px;top:48px" viewBox="0 0 76 84" aria-hidden="true"><use href="#hex-dark"/><g fill="#fff"><rect x="28" y="44" width="20" height="9"/><rect x="30" y="38" width="16" height="6"/><rect x="32" y="33" width="2" height="5"/><rect x="37" y="33" width="2" height="5"/><rect x="42" y="33" width="2" height="5"/></g></svg>
  <div class="stem" style="left:380px;top:130px;height:48px"></div>
  <svg class="hex" style="left:380px;top:48px" viewBox="0 0 76 84" aria-hidden="true"><use href="#hex-dark"/><path d="M30 33h16v10c0 6-4 9-8 11-4-2-8-5-8-11z" fill="#fff"/><path d="M33 36h5v14c-3-2-5-4-5-7z" fill="var(--navy)"/></svg>
  <div class="stem" style="left:644px;top:130px;height:48px"></div>
  <svg class="hex" style="left:644px;top:48px" viewBox="0 0 76 84" aria-hidden="true"><use href="#hex-dark"/><path d="M32 31h12v3h-2v7l4 4v2H30v-2l4-4v-7h-2z M37 47h2v8h-2z" fill="#fff"/></svg>

  <div class="milestone top" style="left:252px;top:76px">Umzug<br>Saarbrücken</div>
  <div class="milestone top" style="left:518px;top:76px">Spezialisierung<br>Cyber Security &amp;<br>Compliance</div>
  <div class="milestone top" style="left:782px;top:76px;font-weight:600;color:var(--sky)">Eröffnung<br>SOC Luxemburg</div>

  <div class="milestone bottom" style="left:114px;top:226px">Gründung<br>Korvanta GmbH</div>
  <div class="milestone bottom" style="left:381px;top:226px">Fokussierung<br>Cyber Security</div>
  <div class="milestone bottom" style="left:648px;top:226px">Transformation<br>Korvanta S.à r.l.</div>

  <!-- bottom milestones -->
  <div class="stem" style="left:248px;top:214px;height:52px"></div>
  <svg class="hex" style="left:248px;top:266px" viewBox="0 0 76 84" aria-hidden="true"><use href="#hex-light"/><path d="M33 34h8v12h5l-7 9-7-9h5v-8h-4z" fill="#fff"/></svg>
  <div class="stem" style="left:512px;top:214px;height:52px"></div>
  <svg class="hex" style="left:512px;top:266px" viewBox="0 0 76 84" aria-hidden="true"><use href="#hex-light"/><path d="M29 34h10v3h-7v14h7v3H29z M36 41h7v-4l8 7-8 7v-4h-7z" fill="#fff"/></svg>
  <div class="stem" style="left:776px;top:214px;height:52px"></div>
  <svg class="hex" style="left:776px;top:266px" viewBox="0 0 76 84" aria-hidden="true"><use href="#hex-light"/><path d="M25 42c4-6 9-8 13-8s9 2 13 8c-4 6-9 8-13 8s-9-2-13-8z" fill="#fff"/><circle cx="38" cy="42" r="4.5" fill="var(--sky)"/></svg>
</div>

<h2 class="company-title">KORVANTA S.À R.L.</h2>
<p class="company-text">Korvanta S.à r.l. ist ein auf IT-Sicherheit und Compliance spezialisiertes Unternehmen. Das etablierte Security Operation Center (SOC) in Luxemburg bietet neben einer optimalen Erreichbarkeit auch Unterstützung bei Sicherheitsüberwachungsdiensten für IT-Infrastrukturen mit verschiedenen Technologien (Logvera, QSentry, Watchtide, Datafold, Scanrift, Shieldmark, Tracewire, Vulnly). Wir bieten somit Dienstleistungen von einer komplexen SIEM-Infrastruktur bis hin zum Schwachstellenmanagement an. Korvanta nutzt die sicherheitsrelevanten Informationen auch, um Use Cases und Reports zur technischen Überwachung der Compliance zu erstellen. Dies kann genutzt werden, um Automatismen zu integrieren, die auf Basis bestehender Infrastrukturkomponenten, wie z. B. Docspace, ein kostengünstiges eGRC abbilden können.</p>
<svg class="company-visual" viewBox="0 0 438 484" role="img" aria-label="Illustration of a glowing security shield with a padlock inside a hexagon frame">
  <defs>
    <radialGradient id="visualGlow" cx="50%" cy="45%" r="60%">
      <stop offset="0" stop-color="#6fc4ff"/>
      <stop offset=".45" stop-color="#1a63c4"/>
      <stop offset="1" stop-color="#0a2d78"/>
    </radialGradient>
  </defs>
  <path d="M219 4 L430 126 Q436 130 436 138 L436 346 Q436 354 430 358 L219 480 L8 358 Q2 354 2 346 L2 138 Q2 130 8 126 Z" fill="none" stroke="var(--navy)" stroke-width="3"/>
  <path d="M219 20 L418 135 L418 349 L219 464 L20 349 L20 135 Z" fill="url(#visualGlow)"/>
</svg>

<footer class="site-footer">
  <div class="footer-brand"><span>Korvanta</span></div>

  <div class="col-rule" style="left:318px"></div>
  <h3 class="col-head" style="left:338px">NAVIGATION</h3>
  <ul class="col-links" style="left:338px"><li>Cdaas</li><li>Security Services</li><li>Compliance</li><li>Unterehmen</li><li>Career</li></ul>

  <div class="col-rule" style="left:502px"></div>
  <h3 class="col-head" style="left:514px">RESOURCES</h3>
  <ul class="col-links" style="left:517px;top:113px"><li>Terms &amp; Condition</li><li>Privacy Policy</li><li>Blogs</li><li>Contact Us</li></ul>

  <div class="col-rule" style="left:692px"></div>
  <h3 class="col-head" style="left:714px">CONTACT US</h3>
  <div class="contact-item" style="left:712px;top:104px">
    <span class="ic"><svg width="16" height="16" viewBox="0 0 16 16"><path d="M3 1l3 3-1.5 2c1 2 3 4 5 5L11.5 9.5l3 3-2 2C7 14 2 9 1.5 3z" fill="var(--footer)"/></svg></span>
    <div><small>Phone Number</small><b>+352 2741 55 10 - 10</b></div>
  </div>
  <div class="contact-item" style="left:716px;top:158px">
    <span class="ic"><svg width="16" height="12" viewBox="0 0 16 12"><rect x="0.5" y="0.5" width="15" height="11" fill="none" stroke="var(--footer)"/><path d="M1 1l7 6 7-6" fill="none" stroke="var(--footer)" stroke-width="1.3"/></svg></span>
    <div><small>Email us</small><b>enquiry@korvanta.lu</b></div>
  </div>

  <div class="col-rule" style="left:921px"></div>
  <h3 class="col-head" style="left:941px">FOLLOW US</h3>
  <div class="socials" aria-label="Social profiles"><i></i><i></i><i></i><i></i></div>

  <div class="footer-rule"></div>
  <p class="copyright">Copyright © 2022 Korvanta. All Rights Reserved</p>
  <p class="legal-links">Privacy | &nbsp;Terms of Use | &nbsp;Legal</p>
</footer>

</body>
</html>
```